integrative health clinic-Medical massage, acupuncture, chiropractic

we like our logo, but are open to new ideas. We need a new card design. We have added chiropractic and acupuncture that we have put under the name of the business. We are an integrative medical clinic

Target Market(s)

General public, athletes

Contact Information for Business Card

Phone 5055583927
Fax 5055583926
Hours Monday-Friday 9-6
Saturday 10-6
The 20% can be smaller on the back

Colors
3176b5
0355a3

Requirements
Must have
• Logo but am open to ideas
Nice to have
• We are an integrated medical clinic but also want to be personable. We want the card fun and inviting

```html
<!DOCTYPE html>
<html lang="en">
<head>
<meta charset="utf-8">
<title>Clearwater Body Health – Business Card</title>
<link rel="stylesheet" href="https://fonts.googleapis.com/css2?family=Montserrat:ital,wght@0,400;0,500;0,600;0,700;1,400;1,700&display=swap">
<style>
  :root {
    --canvas: #ffffff;
    --ink: #1a1a1a;
    --brand-purple: #2e3192;
    --band-dark: #111434;
    --band-light: #2f338c;
    --back-fill: #30348a;
    --white: #ffffff;
  }
  * { margin: 0; padding: 0; box-sizing: border-box; }
  html, body {
    width: 1200px; height: 1200px; overflow: hidden;
    background: var(--canvas);
    font-family: "Montserrat", sans-serif;
  }
  .card {
    position: absolute; left: 244px; width: 712px; height: 408px; overflow: hidden;
  }
  .card-front { top: 159px; background: var(--white); border: 1px solid #333; }
  .card-back { top: 634px; background: var(--back-fill); box-shadow: 4px 4px 4px rgba(0,0,0,0.45); }

  .front-band { position: absolute; left: 0; top: 0; width: 712px; height: 408px; }

  .brand-name {
    position: absolute; left: 0; width: 100%; top: 48px; text-align: center;
    font-weight: 600; font-size: 44px; letter-spacing: -1px; color: var(--ink);
  }
  .brand-tagline {
    position: absolute; left: 250px; top: 107px;
    font-style: italic; font-size: 20px; color: var(--ink);
  }
  .brand-dot {
    position: absolute; left: 172px; top: 106px; width: 30px; height: 30px;
    border-radius: 50%; background: var(--brand-purple);
  }
  .services {
    position: absolute; left: 44px; top: 192px;
    font-weight: 700; font-style: italic; font-size: 20px; color: var(--brand-purple);
  }
  .hours {
    position: absolute; left: 511px; top: 224px;
    font-size: 29px; line-height: 32px; color: var(--brand-purple);
  }
  .contact-list { position: absolute; left: 37px; top: 288px; list-style: none; }
  .contact-item {
    display: flex; align-items: center; height: 27px;
    font-weight: 500; font-size: 15px; color: var(--white);
  }
  .contact-item svg { width: 22px; height: 20px; margin-right: 9px; fill: var(--white); }
  .address {
    position: absolute; left: 398px; top: 333px; width: 290px;
    display: flex; align-items: flex-start;
    font-size: 12.5px; color: var(--white); line-height: 15px;
  }
  .address svg { width: 18px; height: 22px; margin-right: 6px; flex: none; fill: var(--white); }
  .address-text { text-align: center; }

  .book-title {
    position: absolute; left: 0; width: 100%; top: 80px; text-align: center;
    font-weight: 600; font-size: 48px; color: var(--white);
  }
  .book-url {
    position: absolute; left: 0; width: 100%; top: 140px; text-align: center;
    font-weight: 600; font-size: 28px; color: var(--white);
  }
  .offer {
    position: absolute; left: 0; width: 100%; top: 190px; text-align: center;
    font-weight: 700; font-style: italic; font-size: 23px; color: var(--white);
  }
  .back-brand-name {
    position: absolute; left: 38px; top: 262px;
    font-weight: 600; font-size: 34px; letter-spacing: -1px; color: var(--white);
  }
  .back-brand-dot {
    position: absolute; left: 64px; top: 312px; width: 24px; height: 24px;
    border-radius: 50%; background: var(--white);
  }
  .back-tagline {
    position: absolute; left: 122px; top: 308px;
    font-style: italic; font-size: 17px; color: var(--white);
  }
  .specialties {
    position: absolute; left: 424px; width: 240px; top: 256px; text-align: center;
    font-weight: 600; font-size: 18px; line-height: 24px; color: var(--white);
  }
</style>
</head>
<body>

<section class="card card-front">
  <svg class="front-band" viewBox="0 0 712 408" aria-hidden="true">
    <defs>
      <linearGradient id="bandGradient" x1="0" y1="1" x2="1" y2="0">
        <stop offset="0" stop-color="var(--band-dark)"/>
        <stop offset="1" stop-color="var(--band-light)"/>
      </linearGradient>
    </defs>
    <path d="M0 274 C 70 252, 170 246, 300 266 S 520 320, 712 302 L 712 408 L 0 408 Z" fill="url(#bandGradient)"/>
  </svg>

  <h1 class="brand-name">Clearwater Body Health</h1>
  <span class="brand-dot"></span>
  <p class="brand-tagline">Sports Therapy and Wellness Center</p>

  <p class="services">chiropractic and acupuncture</p>
  <p class="hours">Mon-Fri 9-6<br>Sat 10-6</p>

  <ul class="contact-list">
    <li class="contact-item">
      <svg viewBox="0 0 24 24"><path d="M6.6 10.8a15.1 15.1 0 0 0 6.6 6.6l2.2-2.2a1 1 0 0 1 1-.25 11.4 11.4 0 0 0 3.6.57 1 1 0 0 1 1 1V20a1 1 0 0 1-1 1A17 17 0 0 1 3 4a1 1 0 0 1 1-1h3.5a1 1 0 0 1 1 1c0 1.25.2 2.45.57 3.57a1 1 0 0 1-.25 1z"/></svg>
      (505) 558 3927
    </li>
    <li class="contact-item">
      <svg viewBox="0 0 24 22"><path d="M6 1h10l2 2v5H6z M1 9h22v12H1z" /><circle cx="5" cy="17" r="1.6" fill="#1b1e4a"/></svg>
      5055583926
    </li>
    <li class="contact-item">
      <svg viewBox="0 0 24 22"><path d="M2 2h4l6 9 6-9h4v18h-4V9l-6 8-6-8v11H2z"/></svg>
      info@clearwaterbodyhealth.com
    </li>
  </ul>

  <div class="address">
    <svg viewBox="0 0 18 22"><path d="M9 0a8 8 0 0 0-8 8c0 6 8 14 8 14s8-8 8-14a8 8 0 0 0-8-8zm0 11a3 3 0 1 1 0-6 3 3 0 0 1 0 6z"/></svg>
    <span class="address-text">4410 Mesa Verde Lane, Suite 3 Santa Fe NM ,<br>87507</span>
  </div>
</section>

<section class="card card-back">
  <h2 class="book-title">Book Online</h2>
  <p class="book-url">www.clearwaterbodyhealth.com</p>
  <p class="offer">20% off first visit</p>

  <p class="back-brand-name">Clearwater Body Health</p>
  <span class="back-brand-dot"></span>
  <p class="back-tagline">Sports Therapy and Wellness Center</p>

  <p class="specialties">Specializing in Medical<br>Sports Massage<br>and Manual Therapies</p>
</section>

</body>
</html>
```